QZN Supplements needs a label designer for supplement company

Looking for an on going label designer for my supplement company. I have three products that will need designs. I'm about to launch my sleep supplement called Velmora Rest and that's the first design needed.
I would like all designs to be somewhat simple, not overstated and uniformed so that when you look at all of the labels of the different supplements they are similar and you can tell it's the same brand.
Please see attached sample pictures below as ideas.
Updates

The brand is QZN supplements, logo file has been provided. The supplement is called Velmora Rest. It is a liquid supplement that is a 32/33 ounce white bottle. Die lines and measurements will be provided. Here's text for wording ideas: Wording: Natural Sleep Aid Reset your circadian rhythm. May help you: Fall asleep faster. Get a deeper more restful sleep. Boost Immune System Remember your dreams. Protect your brain and flush toxins. Wake up feeling refreshed. Non-gmo Gluten Free Sugar Free Vegan Manufactured in cGMP factory Manufactured in USA

Target Market(s)

Health and wellness/supplement industry for regular people not hardcore gym goers. My supplements are for a health lifestyle not bodybuilding.

Industry/Entity Type

Health And Wellness

Colors
3176b5
3276b5
33a6d7
85cae6
85abd2
cedeed
e4daeb
b7a5cd

Requirements
Must have
• There will be some text and wording that I will provide that must be on the bottles.

```html
<!DOCTYPE html>
<html lang="en">
<head>
<meta charset="utf-8">
<title>Velmora Rest – QZN Supplements Label</title>
<link rel="stylesheet" href="https://fonts.googleapis.com/css2?family=Oswald:wght@300;400;600;700&family=Roboto+Condensed:wght@500;700&display=swap">
<style>
  :root {
    --page: #ffffff;
    --night-top: #0f1a4d;
    --night-mid: #2c2a5c;
    --dusk: #5a4a6e;
    --haze: #a88aa6;
    --blush: #e9c6d6;
    --white: #ffffff;
    --ink: #2e2a4a;
    --brain: #33a6d7;
    --brain-light: #85cae6;
    --frame: rgba(255, 255, 255, 0.75);
  }
  * { margin: 0; padding: 0; box-sizing: border-box; }
  html, body {
    width: 1031px;
    height: 1200px;
    overflow: hidden;
    background: var(--page);
  }
  .canvas {
    position: relative;
    width: 1031px;
    height: 1200px;
  }
  .label {
    position: absolute;
    left: 215px;
    top: 80px;
    width: 600px;
    height: 1040px;
    background: linear-gradient(180deg,
      var(--night-top) 0%,
      var(--night-mid) 30%,
      var(--dusk) 60%,
      var(--haze) 82%,
      var(--blush) 100%);
    overflow: hidden;
  }
  .label__frame {
    position: absolute;
    left: 30px;
    top: 230px;
    width: 540px;
    height: 630px;
    border: 2px solid var(--frame);
    border-radius: 6px;
  }
  .brand-badge {
    position: absolute;
    left: 70px;
    top: 250px;
    width: 460px;
    height: 72px;
    background: var(--white);
    border-radius: 18px;
    display: flex;
    align-items: center;
    justify-content: center;
    gap: 14px;
  }
  .brand-badge__dot {
    width: 34px;
    height: 34px;
    border-radius: 50%;
    border: 3px solid var(--ink);
  }
  .brand-badge__name {
    font-family: "Oswald", sans-serif;
    font-weight: 600;
    font-size: 30px;
    line-height: 1;
    letter-spacing: 0.5px;
    color: var(--ink);
  }
  .sleep-mark {
    position: absolute;
    left: 380px;
    top: 345px;
    width: 80px;
    height: 70px;
    font-family: "Oswald", sans-serif;
    font-weight: 700;
    color: var(--white);
    line-height: 1;
  }
  .sleep-mark span { position: absolute; }
  .sleep-mark .z1 { left: 0; top: 36px; font-size: 30px; }
  .sleep-mark .z2 { left: 22px; top: 18px; font-size: 24px; }
  .sleep-mark .z3 { left: 40px; top: 2px; font-size: 18px; }
  .brain-art {
    position: absolute;
    left: 205px;
    top: 420px;
    width: 190px;
    height: 145px;
    border-radius: 50% 50% 45% 45%;
    background: radial-gradient(circle at 45% 40%, var(--brain-light), var(--brain) 70%);
  }
  .product-name {
    position: absolute;
    left: 0;
    top: 596px;
    width: 600px;
    text-align: center;
    color: var(--white);
    font-family: "Oswald", sans-serif;
  }
  .product-name__first {
    display: block;
    font-weight: 300;
    font-size: 62px;
    line-height: 66px;
    letter-spacing: 1px;
  }
  .product-name__second {
    display: block;
    font-weight: 700;
    font-size: 86px;
    line-height: 92px;
  }
  .tagline {
    position: absolute;
    left: 60px;
    top: 775px;
    width: 480px;
    text-align: center;
    font-family: "Roboto Condensed", sans-serif;
    font-weight: 700;
    font-size: 19px;
    line-height: 24px;
    color: var(--white);
  }
  .supplement-type {
    position: absolute;
    left: 0;
    top: 905px;
    width: 600px;
    text-align: center;
    font-family: "Roboto Condensed", sans-serif;
    font-weight: 700;
    font-size: 30px;
    line-height: 1;
    color: var(--ink);
  }
</style>
</head>
<body>
<main class="canvas">
  <section class="label">
    <div class="label__frame"></div>

    <div class="brand-badge">
      <span class="brand-badge__dot"></span>
      <span class="brand-badge__name">QZN SUPPLEMENTS</span>
    </div>

    <div class="sleep-mark" aria-hidden="true">
      <span class="z1">z</span><span class="z2">z</span><span class="z3">z</span>
    </div>

    <div class="brain-art" role="img" aria-label="Glowing blue brain illustration"></div>

    <h1 class="product-name">
      <span class="product-name__first">VELMORA</span>
      <span class="product-name__second">REST</span>
    </h1>

    <p class="tagline">Relaxes You &amp; Keeps You Asleep So You<br>Wake Up Feeling Refreshed</p>

    <p class="supplement-type">Dietary Supplement</p>
  </section>
</main>
</body>
</html>
```